Local massage therapist needs some new marketing material

Hi there! I am a massage therapist here in Denver, CO in Willow Basin(shopping and art district) of the city. My business is called Lotus Drift Massage of Denver. My practice has an eastern influence and I do reflexology, thai massage and use Chinese herbs, etc. I know all my clients and pay close attention to details. I am also very respectful of tradition and it shows in how I work. I tend to like modern, clean, fun, Asian designs. I am wanting a new business card and brochure. I have a logo and branding for my business that I want used in the design. Currently, the sign for my building is purple and I think my logo was designed to be purple. I will attach pictures of it and can send whatever files are necessary so it can be integrated into the brochure, etc. I like the purple but open to using other colors as well. Thanks!
My website is lotusdriftmassagehub.example where info can be gathered about me and services/fees for brochure.
Updates

Just increased budget. Please see new feedback in discussion thread.

Thanks!

                                       HEY ALL,

Just wanted to let you know that I made a change to my website. It is on the Prices Page. I no longer have the frequent  flyer prices but I added discounts. Let me know if you have any questions. Thanks so much!

Target Market(s)

healthy, urban, educated, upper middle class, yogis

Industry/Entity Type

Marketing

Requirements
Must have
• logo stays purple
Should not have
• not too busy

```html
<!DOCTYPE html>
<html lang="en">
<head>
<meta charset="utf-8">
<title>Lotus Drift Massage of Denver – Brochure</title>
<link href="https://fonts.googleapis.com/css2?family=Oswald:wght@500;600&family=Roboto+Condensed:wght@400;700&family=Montserrat:wght@300&display=swap" rel="stylesheet">
<style>
:root{
  --bg:#e9e9e9;
  --green:#8dc63f;
  --green-dark:#74ab2c;
  --green-ink:#2f4a12;
  --green-pale:#d4eba0;
  --green-paler:#e3f2c0;
  --purple:#5c2b8a;
  --purple-deep:#4a1f73;
  --purple-mid:#7a4fa8;
  --purple-soft:#a385c6;
  --white:#ffffff;
  --ink:#333333;
}
*{box-sizing:border-box;margin:0;padding:0}
html,body{width:1200px;height:1000px;overflow:hidden;background:var(--bg)}
body{font-family:"Roboto Condensed",Arial,sans-serif;color:var(--ink);position:relative}
p{font-size:10.5px;line-height:1.36}
.spread{position:absolute;left:40px;display:flex;box-shadow:0 4px 14px rgba(0,0,0,.15)}
.spread--inside{top:18px;height:606px}
.spread--outside{top:642px;height:340px}
.panel{width:373.3px;height:100%;position:relative;overflow:hidden}

/* inside panel 1 */
.panel--about{background:var(--green);display:flex;flex-direction:column}
.about-top{padding:16px 18px 10px}
.panel-title{font-family:"Oswald",Arial,sans-serif;font-weight:600;font-size:21px;text-transform:uppercase;letter-spacing:.2px}
.panel--about .panel-title{color:var(--green-ink);margin-bottom:10px}
.bio-photo{float:left;width:76px;height:88px;margin:0 10px 4px 0;background:linear-gradient(160deg,#d8b98a,#a77a58 60%,#5a7fa0);border:2px solid var(--white)}
.bio-name{font-family:"Oswald",Arial,sans-serif;font-weight:500;font-size:19px;color:var(--white);line-height:1.1}
.panel--about p{color:var(--green-ink)}
.about-thai{flex:1;background:var(--green-dark);padding:12px 18px}
.about-thai .panel-title{font-size:17px;color:var(--white);margin-bottom:6px;text-align:center}
.about-thai p{color:var(--white)}

/* inside panel 2 */
.panel--services{background:var(--green-pale)}
.services-head{background:var(--green-paler);height:58px;display:flex;align-items:center;justify-content:center}
.panel--services .panel-title{color:var(--green-ink)}
.service{padding:10px 18px 12px;border-bottom:1px solid rgba(47,74,18,.18)}
.service:nth-child(odd){background:var(--green-paler)}
.service-title,.treat-title{font-weight:700;font-size:11px;text-transform:uppercase;text-align:center;margin-bottom:5px}
.service-title{color:var(--green-ink)}

/* inside panel 3 */
.panel--treats{background:var(--purple-soft);color:var(--white);display:flex;flex-direction:column}
.treats-head{background:var(--purple-mid);height:58px;display:flex;align-items:center;justify-content:center}
.treat{padding:8px 18px 6px}
.treat p{color:var(--white)}
.discounts{margin-top:auto;background:var(--purple-mid);padding:10px 18px 14px}
.discounts li{list-style:none;font-size:10.5px;line-height:1.36}

/* outside */
.panel--intro{background:linear-gradient(135deg,#cfcfcf,#8a8a8a 45%,#4a4a4a)}
.intro-box{position:absolute;top:18px;left:18px;width:210px;background:var(--green);padding:10px 12px}
.intro-item{margin-bottom:7px}
.intro-item h3{font-size:10.5px;font-weight:700;text-transform:uppercase;color:var(--white)}
.intro-item p{color:var(--green-ink)}
.panel--contact{background:var(--purple-deep);color:var(--white);display:flex;flex-direction:column;align-items:center;justify-content:flex-end;padding-bottom:30px;text-align:center}
.contact-mark{width:26px;height:26px;background:var(--green);transform:rotate(45deg);margin-bottom:22px}
.contact-phone{font-weight:700;font-size:19px}
.contact-note{font-weight:700;font-size:11px;margin-bottom:10px}
.contact-line{font-size:11px;line-height:1.4}
.panel--cover{background:var(--purple)}
.cover-name{position:absolute;left:0;right:0;top:190px;text-align:center;font-family:"Montserrat",Arial,sans-serif;font-weight:300;font-size:22px;letter-spacing:4px;color:var(--white);text-transform:uppercase;line-height:1.5}
.cover-tri{position:absolute;left:0;width:100%}
.cover-tri--top{top:0}
.cover-tri--bottom{bottom:0}
</style>
</head>
<body>

<section class="spread spread--inside">
  <article class="panel panel--about">
    <div class="about-top">
      <h2 class="panel-title">Lotus Drift Massage of Denver</h2>
      <div class="bio-photo" role="img" aria-label="Portrait of the massage therapist"></div>
      <div class="bio-name">Maya Linden</div>
      <p>is a registered massage therapist, a member of national massage, aromatherapy and Thai healing associations. She graduated from the Front Range Bodywork Institute and has formally studied Thai Massage techniques at the Chiang Valley Training School, Thailand. Presently, she is studying at Open Path Healing Academy with students from around the world to better understand natural health, energy work and spiritual counseling. Maya began meditation as a teen and learned the benefits of quieting the mind. Feeling the call within herself to help others, Maya naturally gravitated toward massage therapy and natural healing. Maya enjoys helping to facilitate people on their journeys toward health and personal growth. She believes in an energy (Chi) within us that, when balanced, promotes our health and well-being. She trusts the body's natural capacity to heal, and takes great care and intention in her delivery of bodywork.</p>
    </div>
    <div class="about-thai">
      <h2 class="panel-title">• Table Thai Massage •</h2>
      <p>Table Thai Massage is an adaptation of the Traditional Thai Massage, performed on a massage table rather than a floor mat. The client is fully clothed and no oil or lotion is used. It combines gentle stretching, compressions, acupressure and assisted yoga postures to help lengthen shortened muscles and bring the body back into a state of balance. Thai massage differs from conventional massage because it does not only work with muscles and soft tissue, but rather it follows energy lines, or Sen lines. The intention is to open the flow along these lines so that, when blockages are released, energy can move freely again and clients leave feeling uplifted and energized.</p>
    </div>
  </article>

  <article class="panel panel--services">
    <header class="services-head"><h2 class="panel-title">Other Massage Services</h2></header>
    <div class="service">
      <h3 class="service-title">• Swedish Escape •</h3>
      <p>Swedish Massage is a very relaxing and therapeutic style of bodywork. It combines oils with an array of strokes such as rolling, kneading, and percussion to help the body improve its circulation. The benefits of this type of bodywork are wide-ranging and include relief from aches and pains, decreased stress levels in the body, enhanced mental clarity, improved appearance, and greater flexibility.</p>
    </div>
    <div class="service">
      <h3 class="service-title">• Deep Tissue Therapy •</h3>
      <p>Deep tissue massage is designed to relieve severe tension in the muscle and the connective tissue. This type of massage focuses on the muscles located below the surface of the top muscles. Deep tissue massage is often recommended for individuals who experience consistent pain, are involved in heavy physical activity, and who have sustained physical injury. It is not uncommon for receivers of deep tissue massage to have their pain replaced with a new muscle ache for a day or two. Multiple sessions may be required in order to see consistent results and meet goals of becoming pain free.</p>
    </div>
    <div class="service">
      <h3 class="service-title">• Prenatal Bliss •</h3>
      <p>Prenatal massage has been found to reduce stress, decrease swelling in the arms and legs, and relieve aches and pains in muscles and joints. Not only can massage be physically beneficial, but the human touch can be comforting and provide emotional support during pregnancy. Massage therapy has been found to reduce anxiety and depression. Massage is best to start during the second trimester.</p>
    </div>
    <div class="service">
      <h3 class="service-title">• Blend Massage •</h3>
      <p>Blend Massage incorporates all techniques into one fully restorative and therapeutic session. Enjoy the benefits of soothing Swedish strokes, attention to Thai Sen lines, gentle stretching and deep pressure to relieve accumulated muscle tension and stress. This is the most popular modality.</p>
    </div>
  </article>

  <article class="panel panel--treats">
    <header class="treats-head"><h2 class="panel-title">Extra Massage Treats</h2></header>
    <div class="treat">
      <h3 class="treat-title">• Chinese Fire Cupping •</h3>
      <p>Cupping Method that uses glass cups to create a vacuum on the skin of the back. The suction penetrates deep into the tissues, allowing them to relax and release toxins. It triggers the lymphatic system, clears the blood vessels, loosens tight muscles, and stimulates the skin.</p>
    </div>
    <div class="treat">
      <h3 class="treat-title">• Hot Stones •</h3>
      <p>Hot stones (local basalt Colorado rocks) incorporates the use of smooth heated stones for a deeply soothing and relaxing experience. The stones are either used as part of a traditional Swedish session or placed along specific areas of muscle tension to reduce discomfort and increase circulation. A nice treat after a long day or during the winter season.</p>
    </div>
    <div class="treat">
      <h3 class="treat-title">• Reflexology •</h3>
      <p>A modality focused on the feet. It is a non-invasive way to work the entire body system. Pressure is applied to various reflexes on the feet in order to promote balance and healing in the body. Certain areas of the foot correspond to organs and specific parts of the body. Reflexology helps to clear blocked energy, balance emotions and relax the body.</p>
    </div>
    <div class="treat">
      <h3 class="treat-title">• Thai Herbal Compress •</h3>
      <p>Hand-made herbal compresses imported from Thailand make for a truly delightful and unique experience. The steamed herbal compress is applied directly to the body and helps relieve sore muscles while the aroma soothes the mind.</p>
    </div>
    <div class="discounts">
      <h3 class="treat-title">• Discounts •</h3>
      <ul>
        <li>• <b>Massage Punch Card:</b> Upon your initial visit, you will receive your first punch. After 9 massages at the regular price, you will earn a free 1 hour massage of your choice.</li>
        <li>• <b>Referral Program:</b> Get $10 off for every referral you make that comes in for a session. Gift certificates purchased for new clients will count toward the discount.</li>
        <li>• <b>Seniors, Students &amp; Educators:</b> Ask about your discount.</li>
      </ul>
    </div>
  </article>
</section>

<section class="spread spread--outside">
  <article class="panel panel--intro" role="img" aria-label="Black and white photo of smooth spa stones with scattered petals">
    <div class="intro-box">
      <div class="intro-item"><h3>• What we offer</h3><p>Prenatal, Swedish and general pain management; there are a variety of services to fit your needs.</p></div>
      <div class="intro-item"><h3>• Experienced therapist</h3><p>Licensed, accredited and very friendly. Maya is committed to your wellness.</p></div>
      <div class="intro-item"><h3>• Make an appointment</h3><p>Book a relaxing massage today.</p></div>
    </div>
  </article>

  <article class="panel panel--contact">
    <div class="contact-mark"></div>
    <div class="contact-phone">555.014.2270</div>
    <div class="contact-note">• Appointments required •</div>
    <div class="contact-line">1480 Juniper Lane, Denver, CO 80000</div>
    <div class="contact-line">info@lotusdriftmassagehub.example</div>
  </article>

  <article class="panel panel--cover">
    <svg class="cover-tri cover-tri--top" viewBox="0 0 373 40" height="40" preserveAspectRatio="none">
      <polygon points="146,0 227,0 186.5,38" fill="#8dc63f"/>
    </svg>
    <div class="cover-name">Lotus Drift<br>Massage</div>
    <svg class="cover-tri cover-tri--bottom" viewBox="0 0 373 60" height="60" preserveAspectRatio="none">
      <polygon points="126,60 186.5,0 247,60" fill="#4a1f73"/>
      <polygon points="140,60 186.5,14 233,60" fill="#8dc63f"/>
    </svg>
  </article>
</section>

</body>
</html>
```